KickHarbor.com Website

We need a dynamic, vibrant and modern design for our new website.

KickHarbor will bridge the generational gap between young and old by bringing together footballers from different generations to play with and against each other, whilst giving fans a unique opportunity to watch them.

Old memories will be passed from parents to children or from grandparents to grandchildren, whilst new memories are created and shared.

The website will provide fans from all over the world with exclusive content, merchandise, tickets and forums on which to exchange their stories, experiences and opinions.

The winning website design needs to be as unique as the product whilst and provide the perfect platform from which to reach, attract and keep as many fans as possible.

Target Market(s)

Worldwide football fans across generations and from different teams.

Number of Pages Required

3 page

Requirements
Must have
• Included KickHarbor logo design as attached. The colours from the logo should also be incorporated throughout the website where possible.
• Home Page, Merchandise Page, Teams Page - screen shots attached for information.
Should not have
• Any reference to or pictures of American Football

```html
<!DOCTYPE html>
<html lang="en">
<head>
<meta charset="utf-8">
<title>KickHarbor – Merchandise</title>
<link href="https://fonts.googleapis.com/css2?family=Open+Sans:wght@400;600;700;800&display=swap" rel="stylesheet">
<style>
:root{
  --white:#ffffff;
  --ink:#1d2733;
  --nav:#4b5563;
  --blue:#2a6db5;
  --red:#e0262c;
  --teal:#3f8b9b;
  --teal-dark:#2f6f7d;
  --bar-dark:#15191e;
  --select:#3a4049;
  --footer:#1b222b;
  --footer-deep:#12171d;
  --footer-text:#9aa4af;
}
*{margin:0;padding:0;box-sizing:border-box}
html,body{width:690px;height:1200px;overflow:hidden}
body{font-family:'Open Sans',Arial,sans-serif;background:var(--white);color:var(--ink);position:relative}

/* header */
.site-header{position:absolute;top:0;left:0;width:690px;height:70px;background:var(--white)}
.brand{position:absolute;left:32px;top:22px;display:flex;align-items:center;gap:7px}
.brand-mark{width:16px;height:16px;background:var(--blue)}
.brand-name{font-size:15px;font-weight:800;color:var(--blue)}
.main-nav{position:absolute;right:50px;top:14px;display:flex;gap:16px}
.main-nav a{font-size:7.5px;font-weight:600;color:var(--nav);text-decoration:none;text-transform:uppercase;padding-bottom:6px;border-bottom:2px solid transparent}
.main-nav a.active{color:var(--ink);border-bottom-color:var(--red)}
.search-icon{position:absolute;right:18px;top:11px}

/* intro */
.page-title{position:absolute;top:92px;width:100%;text-align:center;font-size:8px;font-weight:700;color:var(--red);text-transform:uppercase;letter-spacing:.3px}
.page-intro{position:absolute;top:106px;left:135px;width:420px;text-align:center;font-size:8px;line-height:13px;color:var(--blue)}
.filters{position:absolute;top:146px;left:0;width:690px;display:flex;justify-content:center;gap:8px}
.select{width:150px;height:18px;background:var(--select);color:var(--white);font-size:7px;line-height:18px;padding-left:8px;position:relative}
.select::after{content:"";position:absolute;right:0;top:0;width:18px;height:18px;background:var(--ink)}
.select .caret{position:absolute;right:5px;top:7px;z-index:1}

/* product grid */
.product-grid{position:absolute;top:195px;left:58px;display:grid;grid-template-columns:repeat(4,127px);column-gap:20px;row-gap:78px}
.product-card{position:relative;width:127px;height:112px;background:var(--teal)}
.product-card::before{content:"";position:absolute;top:-10px;left:18px;right:18px;height:10px;border:1px solid var(--red);border-bottom:none}
.product-shot{height:90px;display:flex;align-items:center;justify-content:center;background:linear-gradient(160deg,var(--teal),var(--teal-dark))}
.product-shot div{width:74px;height:58px;border-radius:6px}
.product-bar{display:flex;height:22px;font-size:7px;font-weight:700;color:var(--white);text-transform:uppercase}
.price{width:38px;background:var(--red);line-height:22px;text-align:center}
.cart{flex:1;background:var(--bar-dark);line-height:22px;text-align:center}

/* footer */
.site-footer{position:absolute;top:975px;left:0;width:690px;height:225px;background:linear-gradient(180deg,var(--footer),var(--footer-deep))}
.footer-brand{position:absolute;left:30px;top:32px;display:flex;align-items:center;gap:7px}
.footer-brand .brand-name{color:var(--white)}
.footer-about{position:absolute;left:30px;top:88px;width:185px;font-size:7px;line-height:11px;color:var(--footer-text)}
.footer-col h3{font-size:8px;font-weight:700;color:var(--white);text-transform:uppercase;margin-bottom:10px}
.services{position:absolute;left:250px;top:28px}
.services ul{list-style:none;display:grid;grid-template-columns:80px 80px;row-gap:7px}
.services li{font-size:6.5px;color:var(--footer-text)}
.services li::before{content:"› ";color:var(--red);font-weight:700}
.newsletter{position:absolute;left:450px;top:28px;width:210px}
.newsletter p{font-size:7px;line-height:11px;color:var(--footer-text);margin-bottom:9px}
.subscribe{display:flex;height:18px;width:150px}
.subscribe span{flex:1;background:var(--white);font-size:6.5px;line-height:18px;padding-left:6px;color:#8a929b}
.subscribe b{width:20px;background:var(--red);display:flex;align-items:center;justify-content:center}
.stay{font-size:6.5px;font-weight:700;color:var(--white);text-transform:uppercase;margin:12px 0 6px}
.social{display:flex;gap:6px}
.social i{width:13px;height:13px;border:1px solid var(--footer-text)}
.copyright{position:absolute;bottom:0;left:0;width:690px;height:24px;background:var(--footer-deep);border-top:1px solid #2a333e;font-size:6.5px;line-height:24px;text-align:center;color:var(--footer-text)}
</style>
</head>
<body>

<header class="site-header">
  <div class="brand"><span class="brand-mark"></span><span class="brand-name">KickHarbor</span></div>
  <nav class="main-nav">
    <a href="#">Home</a>
    <a href="#">Latest News</a>
    <a href="#">Teams</a>
    <a href="#" class="active">Merchandise</a>
    <a href="#">Competitions</a>
    <a href="#">Tickets</a>
    <a href="#">Login · Sign Up</a>
  </nav>
  <svg class="search-icon" width="16" height="16" viewBox="0 0 16 16"><circle cx="6.5" cy="6.5" r="4.8" fill="none" stroke="#2a6db5" stroke-width="2"/><line x1="10" y1="10" x2="14.5" y2="14.5" stroke="#2a6db5" stroke-width="2.4" stroke-linecap="round"/></svg>
</header>

<h1 class="page-title">Merchandise Page</h1>
<p class="page-intro">Browse official kit, boots and keepsakes from every generation of players. Each item ships worldwide and helps bring fans of all ages together on match day.</p>

<div class="filters">
  <div class="select">Sort by Default Order<svg class="caret" width="8" height="5" viewBox="0 0 8 5"><path d="M0 0h8L4 5z" fill="#fff"/></svg></div>
  <div class="select">Show 12 Products Per Page<svg class="caret" width="8" height="5" viewBox="0 0 8 5"><path d="M0 0h8L4 5z" fill="#fff"/></svg></div>
</div>

<main class="product-grid">
  <article class="product-card"><div class="product-shot"><div role="img" aria-label="Red home football jersey" style="background:linear-gradient(#d1222a,#9e1419)"></div></div><div class="product-bar"><span class="price">$ xyz</span><span class="cart">Add to cart</span></div></article>
  <article class="product-card"><div class="product-shot"><div role="img" aria-label="Orange football boot" style="background:linear-gradient(#f48a1f,#c4560c)"></div></div><div class="product-bar"><span class="price">$ xyz</span><span class="cart">Add to cart</span></div></article>
  <article class="product-card"><div class="product-shot"><div role="img" aria-label="Navy football jersey" style="background:linear-gradient(#263a6a,#131f3d)"></div></div><div class="product-bar"><span class="price">$ xyz</span><span class="cart">Add to cart</span></div></article>
  <article class="product-card"><div class="product-shot"><div role="img" aria-label="Black and white football boot" style="background:linear-gradient(#e8e8e8,#222)"></div></div><div class="product-bar"><span class="price">$ xyz</span><span class="cart">Add to cart</span></div></article>

  <article class="product-card"><div class="product-shot"><div role="img" aria-label="Red and white football jersey" style="background:linear-gradient(90deg,#f2f2f2 15%,#d1222a 15%,#d1222a 85%,#f2f2f2 85%)"></div></div><div class="product-bar"><span class="price">$ xyz</span><span class="cart">Add to cart</span></div></article>
  <article class="product-card"><div class="product-shot"><div role="img" aria-label="Black and white football boot" style="background:linear-gradient(#f4f4f4,#1c1c1c)"></div></div><div class="product-bar"><span class="price">$ xyz</span><span class="cart">Add to cart</span></div></article>
  <article class="product-card"><div class="product-shot"><div role="img" aria-label="Yellow fan t-shirt with ball print" style="background:linear-gradient(#f7c21c,#e6a20a)"></div></div><div class="product-bar"><span class="price">$ xyz</span><span class="cart">Add to cart</span></div></article>
  <article class="product-card"><div class="product-shot"><div role="img" aria-label="Grey and orange football boot" style="background:linear-gradient(#d9d9d9,#e2682a)"></div></div><div class="product-bar"><span class="price">$ xyz</span><span class="cart">Add to cart</span></div></article>

  <article class="product-card"><div class="product-shot"><div role="img" aria-label="Yellow and black football boot" style="background:linear-gradient(#e8d418,#1e1e1e)"></div></div><div class="product-bar"><span class="price">$ xyz</span><span class="cart">Add to cart</span></div></article>
  <article class="product-card"><div class="product-shot"><div role="img" aria-label="White and light blue striped jersey" style="background:linear-gradient(90deg,#f3f6f9,#9fc4e6,#f3f6f9)"></div></div><div class="product-bar"><span class="price">$ xyz</span><span class="cart">Add to cart</span></div></article>
  <article class="product-card"><div class="product-shot"><div role="img" aria-label="Pink football boot" style="background:linear-gradient(#ef3f8e,#b81d63)"></div></div><div class="product-bar"><span class="price">$ xyz</span><span class="cart">Add to cart</span></div></article>
  <article class="product-card"><div class="product-shot"><div role="img" aria-label="White t-shirt with red and navy sleeves" style="background:linear-gradient(90deg,#c4262e 18%,#f5f5f5 18%,#f5f5f5 82%,#1f2d5a 82%)"></div></div><div class="product-bar"><span class="price">$ xyz</span><span class="cart">Add to cart</span></div></article>

  <article class="product-card"><div class="product-shot"><div role="img" aria-label="Yellow and green fan t-shirt" style="background:linear-gradient(#f2dc12,#2f9a3c)"></div></div><div class="product-bar"><span class="price">$ xyz</span><span class="cart">Add to cart</span></div></article>
  <article class="product-card"><div class="product-shot"><div role="img" aria-label="Orange and black football boot" style="background:linear-gradient(#f2801c,#1b1b1b)"></div></div><div class="product-bar"><span class="price">$ xyz</span><span class="cart">Add to cart</span></div></article>
  <article class="product-card"><div class="product-shot"><div role="img" aria-label="White and green football jersey" style="background:linear-gradient(#f4f4f4,#2e8b4a)"></div></div><div class="product-bar"><span class="price">$ xyz</span><span class="cart">Add to cart</span></div></article>
</main>

<footer class="site-footer">
  <div class="footer-brand"><span class="brand-mark"></span><span class="brand-name">KickHarbor</span></div>
  <p class="footer-about">KickHarbor brings footballers from different generations together to play with and against each other, giving fans a unique chance to watch old and new memories made.</p>

  <div class="footer-col services">
    <h3>Our Service</h3>
    <ul>
      <li>Match Tickets</li><li>Team Kits</li>
      <li>Fan Forums</li><li>Legends Games</li>
      <li>Exclusive Videos</li><li>Player Stories</li>
      <li>Club News</li><li>Youth Camps</li>
      <li>Gift Cards</li><li>Live Scores</li>
      <li>Shipping Info</li><li>Contact Us</li>
    </ul>
  </div>

  <div class="footer-col newsletter">
    <h3>Newsletter</h3>
    <p>Sign up for the latest news, ticket releases and exclusive offers from KickHarbor.</p>
    <div class="subscribe"><span>Enter your email address</span><b><svg width="9" height="9" viewBox="0 0 9 9"><path d="M0 4.5L9 0 6.5 9 4.5 5.5z" fill="#fff"/></svg></b></div>
    <div class="stay">Stay Connected</div>
    <div class="social"><i></i><i></i><i></i><i></i><i></i></div>
  </div>

  <div class="copyright">© 2016 KickHarbor. All Rights Reserved</div>
</footer>

</body>
</html>
```